Velmor Glazing

Modern glazing company specializing in commercial fit outs, pool fencing, frameless showers and glass splash backs, im after a very young/modern logo, it doesnt have to be revelent to glazing and a classy "boss like" design for the card. thank you in advanced

im thinking carbon fiber back ground or something along that line with bright orange wording or something maybe, open to suggestions 

Fencing

company name, name, phone and products

```html
<!DOCTYPE html>
<html lang="en">
<head>
<meta charset="UTF-8">
<title>Velmor Glazing – Business Card</title>
<link rel="stylesheet" href="https://fonts.googleapis.com/css2?family=Oswald:wght@400;500;600&display=swap">
<style>
  :root {
    --page-bg: #e9e7e3;
    --card-dark: #1f2022;
    --card-mid: #2b2c2f;
    --silver: #c9cbce;
    --silver-dim: #8e9196;
    --silver-bright: #eef0f2;
    --orange: #f39a1e;
    --shadow: rgba(0, 0, 0, 0.22);
  }

  * { margin: 0; padding: 0; box-sizing: border-box; }

  html, body {
    width: 1200px;
    height: 784px;
    overflow: hidden;
    background: var(--page-bg);
    font-family: "Oswald", "Arial Narrow", sans-serif;
  }

  .sheet {
    width: 1200px;
    height: 784px;
    display: flex;
    align-items: center;
    justify-content: center;
    gap: 40px;
  }

  .card {
    position: relative;
    width: 540px;
    height: 310px;
    border-radius: 4px;
    background: radial-gradient(ellipse at 50% 40%, var(--card-mid) 0%, var(--card-dark) 75%);
    box-shadow: 0 14px 30px var(--shadow);
    overflow: hidden;
  }

  /* Back: name and phone inside a silver frame */
  .card-back .frame {
    position: absolute;
    inset: 22px;
    border: 3px solid var(--silver);
    box-shadow: inset 0 0 0 5px var(--card-dark), inset 0 0 0 6px var(--silver-dim);
  }

  .contact {
    position: absolute;
    inset: 0;
    display: flex;
    flex-direction: column;
    align-items: center;
    justify-content: center;
    gap: 26px;
    padding-bottom: 30px;
  }

  .contact-name {
    color: var(--silver);
    font-size: 22px;
    font-weight: 500;
    letter-spacing: 9px;
    text-transform: uppercase;
  }

  .contact-phone {
    color: var(--silver-dim);
    font-size: 21px;
    font-weight: 500;
    letter-spacing: 8px;
  }

  /* Front: company name */
  .card-front .brand {
    position: absolute;
    inset: 0;
    display: flex;
    align-items: center;
    justify-content: center;
    gap: 18px;
    padding-left: 70px;
  }

  .brand-square {
    width: 46px;
    height: 46px;
    background: var(--silver);
    flex-shrink: 0;
  }

  .brand-name {
    color: var(--orange);
    font-size: 36px;
    font-weight: 600;
    letter-spacing: 5px;
    text-transform: uppercase;
    line-height: 1;
  }
</style>
</head>
<body>
  <main class="sheet">
    <section class="card card-back" aria-label="Card back">
      <div class="frame"></div>
      <div class="contact">
        <p class="contact-name">Dane Whitlock</p>
        <p class="contact-phone">0400 555 218</p>
      </div>
    </section>

    <section class="card card-front" aria-label="Card front">
      <div class="brand">
        <span class="brand-square"></span>
        <h1 class="brand-name">Velmor Glazing</h1>
      </div>
    </section>
  </main>
</body>
</html>
```